Holvern Incorporated

Holvern is a business that provides consulting, and manages and supplies trades persons in the construction and heavy industries sector. We build, do maintenance, install machinery, and can manage projects or jobs. Would like or prefer more clean, classic designs. Blacks/greys, but open to almost anything.

Target Market(s)

Industrial/Construction/Manufacturing

Industry/Entity Type

Construction Company

Contact Information for Business Card

Clean, business name on the front, possibly have the details on the back, but open to any ideas.

Logo Text

We currently do not have a slogan, open to ideas

Font styles to use
Serif
Sans Serif

Colors

Designer to choose colors to be used in the design.

Requirements
Should not have
• the oval is not my logo, was just an idea. please don't send 20 designs with the oval

```html
<!DOCTYPE html>
<html lang="en">
<head>
<meta charset="utf-8">
<title>Holvern Incorporated – Business Cards</title>
<link rel="stylesheet" href="https://fonts.googleapis.com/css2?family=Zilla+Slab:wght@600&family=Roboto:wght@400;700&display=swap">
<style>
  :root {
    --backdrop: #3b3b3b;
    --ink-black: #0b0b0b;
    --paper-white: #ffffff;
    --arc-grey: #9c9899;
    --text-dark: #1a1a1a;
    --text-mid: #3a3a3a;
    --icon-grey: #8a8a8a;
  }
  * { margin: 0; padding: 0; box-sizing: border-box; }
  html, body {
    width: 1200px; height: 800px; overflow: hidden;
    background: var(--backdrop);
  }
  .canvas {
    position: relative; width: 1200px; height: 800px;
    display: flex; flex-direction: column; align-items: center; justify-content: center;
    gap: 40px;
  }
  .card {
    position: relative; width: 560px; height: 320px; overflow: hidden;
    box-shadow: 0 10px 24px rgba(0,0,0,.45);
  }
  .card-front {
    background: var(--ink-black);
    display: flex; align-items: center; justify-content: center;
  }
  .brand-name {
    font-family: "Zilla Slab", Georgia, serif;
    font-weight: 600; letter-spacing: 1px; line-height: 1;
  }
  .card-front .brand-name { color: var(--paper-white); font-size: 68px; }
  .card-back { background: var(--paper-white); }
  .card-back .backdrop-shape { position: absolute; inset: 0; }
  .card-back .brand-name {
    position: absolute; left: 225px; top: 98px;
    color: var(--ink-black); font-size: 50px;
  }
  .person {
    position: absolute; right: 262px; top: 184px; text-align: right;
    font-family: "Roboto", Arial, sans-serif;
  }
  .person-name { font-weight: 700; font-size: 19px; color: var(--text-dark); }
  .person-role { font-size: 15px; color: var(--text-mid); margin-top: 2px; }
  .divider {
    position: absolute; left: 312px; top: 158px; width: 1.5px; height: 72px;
    background: var(--text-dark);
  }
  .contacts {
    position: absolute; left: 326px; top: 160px; list-style: none;
    font-family: "Roboto", Arial, sans-serif; font-size: 14.5px; color: var(--text-mid);
  }
  .contacts li { display: flex; align-items: center; gap: 8px; height: 22px; }
  .contacts svg { width: 13px; height: 13px; fill: var(--icon-grey); flex: none; }
  .address {
    position: absolute; left: 0; right: 0; top: 272px; text-align: center;
    padding-left: 120px;
    font-family: "Roboto", Arial, sans-serif; font-size: 15px; color: var(--text-dark);
  }
</style>
</head>
<body>
<main class="canvas">
  <section class="card card-front">
    <span class="brand-name">Holvern</span>
  </section>

  <section class="card card-back">
    <svg class="backdrop-shape" viewBox="0 0 560 320" width="560" height="320" aria-hidden="true">
      <rect width="560" height="320" fill="var(--ink-black)"/>
      <ellipse cx="428" cy="334" rx="452" ry="256" fill="var(--arc-grey)"/>
      <ellipse cx="432" cy="336" rx="444" ry="244" fill="var(--paper-white)"/>
    </svg>
    <span class="brand-name">Holvern</span>

    <div class="person">
      <p class="person-name">Dorian Pell</p>
      <p class="person-role">Manager</p>
    </div>
    <span class="divider"></span>
    <ul class="contacts">
      <li>
        <svg viewBox="0 0 24 24"><path d="M6.6 10.8a15.1 15.1 0 0 0 6.6 6.6l2.2-2.2c.3-.3.7-.4 1-.2 1.1.4 2.3.6 3.6.6.6 0 1 .4 1 1V20c0 .6-.4 1-1 1A17 17 0 0 1 3 4c0-.6.4-1 1-1h3.5c.6 0 1 .4 1 1 0 1.3.2 2.5.6 3.6.1.3 0 .7-.2 1z"/></svg>
        123-456-2100
      </li>
      <li>
        <svg viewBox="0 0 24 24"><path d="M2 5h20v14H2z M2 5l10 8 10-8" fill="none" stroke="var(--icon-grey)" stroke-width="2"/><path d="M3 6l9 7 9-7v12H3z"/></svg>
        youremail@mailbox.com
      </li>
      <li>
        <svg viewBox="0 0 24 24"><circle cx="12" cy="12" r="10"/><path d="M2 12h20M12 2c3 3 3 17 0 20M12 2c-3 3-3 17 0 20" fill="none" stroke="var(--paper-white)" stroke-width="1.6"/></svg>
        www.yourwebsite.com
      </li>
    </ul>
    <p class="address">Your address, city, state, ZIP 0000</p>
  </section>
</main>
</body>
</html>
```